QV - menu design

Hi,

We require elegant menu design for upscale restaurant. Please find attached the logo and the menu items for your reference.

for inspiration, this is a good website: -
http://www.platewhisper.example/bellfoldnotes/about.php

We are very much open for Menu Size suggestions.

unfortunately the place is going under renovation, we don't have updated images to it. the closest look and feel to our place is http://varnelo.example ..

we are also open for creative options on the shape, the styles, etc. as long as it represents the fine dine feel ...

Thanks ...

Dear All,

We wouldlike to extend our apology for not being able to provide feedbacks on everysingle design. We were extremely busy and we have multiple contests opensimultaneously which makes the process even harder.

However,we would like to thank you all for the efforts you have put into designingour menu. It is very much appreciated …

We wishyou all success in your design ventures and we are quite positive that we willbe working with many of you on many projects in the soon future. 

Thanks & Regards,

TLG Team...

 

 

 

Industry/Entity Type

Restaurant

Requirements
Must have
• Please ensure that there are 'some' images in the menu ... this is very important.
Should not have
• IMPORTANT: -

1. Please DO NOT insert any currency sign to the menu
2. Please keep the prices of the menu at the end of the menu items descriptions NOT beside the menu item names. The font of the price should be similar to the menu item description and please DO NOT bold the numbers. the prices should be subtle.

Thank you ...

```html
<!DOCTYPE html>
<html lang="en">
<head>
<meta charset="utf-8">
<title>QV – Menu Design</title>
<link href="https://fonts.googleapis.com/css2?family=Raleway:wght@300;400&family=Arimo:ital,wght@0,700;1,400&display=swap" rel="stylesheet">
<style>
  :root {
    --backdrop: #efe9df;
    --paper: #ebe2cd;
    --paper-edge: #ddd0b4;
    --ink: #8b3a20;
    --heading: #a97c62;
    --rule: #b58a6c;
    --leather-light: #8a4524;
    --leather-dark: #4a1f0e;
    --cover-text: #f4ede4;
  }
  * { margin: 0; padding: 0; box-sizing: border-box; }
  html, body { width: 1200px; height: 1000px; overflow: hidden; background: var(--backdrop); }
  .canvas { position: relative; width: 1200px; height: 1000px; }

  /* Cover */
  .menu-cover {
    position: absolute; left: 105px; top: 300px; width: 400px; height: 400px;
    background: radial-gradient(ellipse at 35% 30%, var(--leather-light), var(--leather-dark) 85%);
    border-radius: 3px;
    display: flex; flex-direction: column; align-items: center; justify-content: center;
    color: var(--cover-text); font-family: "Raleway", sans-serif; font-weight: 300;
  }
  .cover-name { font-size: 34px; letter-spacing: 8px; padding-left: 8px; }
  .cover-sub { font-size: 10px; letter-spacing: 6px; padding-left: 6px; margin-top: 6px; }

  /* Pages */
  .menu-page {
    position: absolute; left: 660px; width: 452px; height: 450px;
    background: radial-gradient(ellipse at 50% 45%, #f0e8d6, var(--paper) 60%, var(--paper-edge));
    overflow: hidden;
  }
  .page-breakfast { top: 35px; }
  .page-sandwiches { top: 520px; }

  .section-title {
    position: absolute; left: 28px; right: 0;
    display: flex; align-items: center;
    font-family: "Raleway", sans-serif; font-weight: 300; font-size: 19px; line-height: 22px;
    color: var(--heading);
  }
  .section-title::after { content: ""; flex: 1; height: 1px; background: var(--rule); margin-left: 4px; }

  .menu-item {
    position: absolute; left: 29px;
    font-family: "Arimo", sans-serif; font-size: 8.8px; line-height: 12px; color: var(--ink);
    white-space: nowrap;
  }
  .item-name { font-weight: 700; }
  .item-desc { font-style: italic; font-weight: 400; }

  .food-photo { position: absolute; }
  .photo-salmon {
    left: 276px; top: 272px; width: 176px; height: 178px;
    background: radial-gradient(ellipse at 50% 42%, #f08a64 0 28%, #a7c26b 48%, transparent 70%),
                linear-gradient(180deg, transparent 62%, #5a3a22 78%, transparent 92%);
  }
  .photo-sandwich {
    left: 282px; top: 135px; width: 170px; height: 158px;
    background: radial-gradient(ellipse at 45% 38%, #7a5a6a 0 20%, #c9a04a 35%, #5b7a3a 48%, transparent 62%),
                linear-gradient(180deg, transparent 76%, #a07040 78%, #c89868 100%);
  }
</style>
</head>
<body>
<div class="canvas">

  <section class="menu-cover" aria-label="Menu cover">
    <div class="cover-name">QUILL VALE</div>
    <div class="cover-sub">CAFE</div>
  </section>

  <section class="menu-page page-breakfast">
    <h2 class="section-title" style="top:26px">The Breakfast</h2>
    <div class="food-photo photo-salmon" role="img" aria-label="Photo of smoked salmon open sandwich with greens"></div>
    <div class="menu-item" style="top:58px">
      <div class="item-name">Butter Croissant</div>
      <div class="item-desc">Served plain with a selection of two jams, a vanilla custard<br>cream, a chocolate Cream and butter curls). 36</div>
    </div>
    <div class="menu-item" style="top:106px">
      <div class="item-name">Cheese Croissant</div>
      <div class="item-desc">Crumbly freshly baked with cheese filling. 29</div>
    </div>
    <div class="menu-item" style="top:145px">
      <div class="item-name">Daily Fresh Eggs</div>
      <div class="item-desc">A choice of poached, scrambled, pan fried, omelet) all served<br>with toasted Bread, mushrooms, roasted tomatoes and chicken<br>sausages. 59</div>
    </div>
    <div class="menu-item" style="top:204px">
      <div class="item-name">Healthy Time</div>
      <div class="item-desc">One choice of hot beverage from our cafe served with fruit salad,<br>natural Yoghurt, whole wheat bread vegetable sandwiches and<br>sugar free biscuits selection. 49</div>
    </div>
    <div class="menu-item" style="top:262px">
      <div class="item-name">Energy Time</div>
      <div class="item-desc">One choice of hot beverage from our cafe served with finger<br>chocolate muffins, and honey and finger chocolate cream with<br>salted cookies. 59</div>
    </div>
    <div class="menu-item" style="top:320px">
      <div class="item-name">Quill Vale Time</div>
      <div class="item-desc">One choice of hot beverage from our cafe served with our<br>selection of scones, Smoked salmon and avocado sandwich,<br>roasted sausages sandwich, grilled vegetables sandwich,<br>selection of our best biscuits. 59</div>
    </div>
    <div class="menu-item" style="top:388px">
      <div class="item-name">The Arabic Breakfast</div>
      <div class="item-desc">Choice of ZattarManakish and Cheese Manakish, served<br>with one choice of hot beverage from our cafe and fresh<br>orange juice. 59</div>
    </div>
  </section>

  <section class="menu-page page-sandwiches">
    <h2 class="section-title" style="top:24px">The Sandwiches</h2>
    <div class="food-photo photo-sandwich" role="img" aria-label="Photo of stacked grilled vegetable sandwich on a wooden board"></div>
    <div class="menu-item" style="top:56px"><div class="item-desc">Grilled Vegetables Sandwich with fresh Goat cheese and<br>chives served with our Homemade spicy garlic mayo. 59</div></div>
    <div class="menu-item" style="top:94px"><div class="item-desc">Butterfish burger with fresh tomato, beef bacon, grilled<br>vegetables and béarnaise sauce.</div></div>
    <div class="menu-item" style="top:134px"><div class="item-desc">Tataki Tuna sandwich with red onion slices, stewed endives<br>and black olives andsultanas pate'. 79</div></div>
    <div class="menu-item" style="top:174px"><div class="item-desc">Beef sirloin steak sandwich with grain mustard, Parmesan<br>cheese and fresh Nashi pears. 79</div></div>
    <div class="menu-item" style="top:212px"><div class="item-desc">The Traditional Club sandwich served with French fries and<br>vegetable chips. 69</div></div>
    <div class="menu-item" style="top:250px"><div class="item-desc">Chicken sandwich with Parmesan cheese slices, sundried<br>tomatoes and mint Flavoredmayo. 69</div></div>

    <h2 class="section-title" style="top:285px">Soup</h2>
    <div class="menu-item" style="top:317px">
      <div class="item-name">Bouillabaisse</div>
      <div class="item-desc">Traditional French Seafood soup, with Saffron and Estragon. 119</div>
    </div>
    <div class="menu-item" style="top:359px">
      <div class="item-name">Barley soup</div>
      <div class="item-desc">With fresh vegetables, tomato smoothie and a hint of garlic oil. 49</div>
    </div>
    <div class="menu-item" style="top:402px">
      <div class="item-name">Beef chili</div>
      <div class="item-desc">Served with Arabic bread, fresh guacamole and spicy black beans. 49</div>
    </div>
  </section>

</div>
</body>
</html>
```